Podcast Marketing Template for LinkedIn

I would like to have graphics to post notices of new podcast episodes on LinkedIn as release new episodes.
The graphics need to be in a template form that can be easily updated by my VA.
Each episode will have a new title and guest.
Two examples of a ROUGH DRAFT of an episode example are attached.
(I do not like these because I think they reflect the standards I have for my brand.)
The posts should be bright and clean and clearly reflect QUALITY of the podcast in the quality of the design. Audience and interviewees are CEOs.
Please refer to my website and podcast art to see brand direction.
www.lennartoswaldadvisory.com
Each

```html
<!DOCTYPE html>
<html lang="en">
<head>
<meta charset="utf-8">
<title>Podcast Template</title>
<link rel="stylesheet" href="https://fonts.googleapis.com/css2?family=Montserrat:wght@500;600;700&family=Red+Hat+Display:wght@500;600;700&display=swap">
<style>
  :root {
    --ink: #000000;
    --paper: #ffffff;
    --brand-blue: #1aa3dc;
    --slate: #2b2f36;
  }
  * { box-sizing: border-box; margin: 0; padding: 0; }
  html, body { width: 1200px; height: 1155px; overflow: hidden; background: var(--paper); }
  body { position: relative; font-family: "Montserrat", Arial, sans-serif; }

  .sheet-header {
    position: absolute; left: 0; top: 0; width: 1200px; height: 269px;
    background: var(--ink); color: var(--paper);
  }
  .sheet-title { position: absolute; left: 56px; top: 30px; font-size: 66px; font-weight: 700; letter-spacing: 1px; }
  .sheet-subtitle { position: absolute; left: 56px; top: 136px; font-size: 42px; font-weight: 500; color: var(--brand-blue); }
  .sheet-size { position: absolute; left: 56px; top: 188px; font-size: 26px; font-weight: 600; }
  .sheet-brand {
    position: absolute; left: 930px; top: 50px; width: 170px; height: 170px;
    border-radius: 50%; background: var(--brand-blue);
  }
  .sheet-brand-name {
    position: absolute; left: 870px; top: 232px; width: 290px; text-align: center;
    font-size: 14px; font-weight: 600; letter-spacing: 2px; color: var(--paper);
  }

  .episode-card { position: absolute; width: 360px; height: 360px; overflow: hidden; background: var(--slate); color: var(--paper); }
  .card-a { left: 215px; top: 325px; }
  .card-b { left: 627px; top: 322px; }
  .card-c { left: 216px; top: 745px; }
  .card-d { left: 627px; top: 745px; }

  .card-backdrop { position: absolute; left: 0; top: 97px; width: 360px; height: 263px; }
  .card-a .card-backdrop { background: linear-gradient(100deg, #0d2e50 0%, #1b4f7c 45%, #7d8289 100%); }
  .card-b .card-backdrop { background: linear-gradient(120deg, #12385f 0%, #2a5f8e 50%, #4a4f57 100%); }
  .card-c .card-backdrop { background: linear-gradient(110deg, #0c2a48 0%, #244f78 50%, #9ca1a8 100%); }
  .card-d .card-backdrop { background: linear-gradient(100deg, #0b2440 0%, #1e4a74 45%, #3c4048 100%); }

  .card-masthead {
    position: absolute; left: 0; top: 0; width: 360px; height: 97px;
    background: var(--ink); border-bottom: 2px solid var(--brand-blue);
  }
  .show-label { position: absolute; left: 20px; top: 10px; font-size: 27px; font-weight: 700; }
  .show-name { position: absolute; left: 20px; top: 48px; font-size: 20px; font-weight: 600; color: var(--brand-blue); }
  .show-tagline { position: absolute; left: 20px; top: 72px; font-size: 13px; font-weight: 500; }
  .masthead-mark {
    position: absolute; left: 277px; top: 14px; width: 66px; height: 66px;
    border-radius: 50%; background: var(--brand-blue);
  }

  .episode-title {
    position: absolute; left: 20px; top: 100px; width: 340px;
    font-family: "Red Hat Display", Arial, sans-serif; font-weight: 600;
    font-size: 48px; line-height: 44px; letter-spacing: -0.2px;
  }

  .guest-portrait {
    position: absolute; left: 14px; top: 258px; width: 76px; height: 76px; border-radius: 50%;
    border: 3px solid var(--brand-blue);
    background: radial-gradient(circle at 50% 40%, #c9a58e 0%, #8a6a58 45%, #3b4a5a 100%);
  }
  .guest-credit { position: absolute; left: 100px; top: 281px; font-size: 11.5px; line-height: 14px; font-weight: 500; }
  .guest-role { color: var(--brand-blue); }

  .card-signature { position: absolute; left: 228px; top: 322px; display: flex; align-items: center; gap: 6px; }
  .signature-dot { width: 20px; height: 20px; border-radius: 50%; background: var(--brand-blue); flex: none; }
  .signature-name { font-size: 9px; line-height: 10px; font-weight: 700; color: var(--paper); letter-spacing: 0.5px; width: 104px; }
</style>
</head>
<body>
  <header class="sheet-header">
    <h1 class="sheet-title">PODCAST</h1>
    <p class="sheet-subtitle">TEMPLATE</p>
    <p class="sheet-size">1080X1080PX</p>
    <div class="sheet-brand"></div>
    <p class="sheet-brand-name">LENNART OSWALD ADVISORY</p>
  </header>

  <article class="episode-card card-a">
    <div class="card-backdrop" role="img" aria-label="Blue-toned business photograph of hands and a rising chart"></div>
    <div class="card-masthead">
      <p class="show-label">PODCAST</p>
      <p class="show-name">CHARTING HEADWAYS</p>
      <p class="show-tagline">A CEO GROWTH AND LEGACY</p>
      <div class="masthead-mark"></div>
    </div>
    <h2 class="episode-title">Technology<br>a Philanthropy<br>in Education</h2>
    <div class="guest-portrait" role="img" aria-label="Guest portrait photograph"></div>
    <p class="guest-credit">With Tomas Reller<br><span class="guest-role">CEO of Veltra</span></p>
    <div class="card-signature"><span class="signature-dot"></span><span class="signature-name">LENNART OSWALD ADVISORY</span></div>
  </article>

  <article class="episode-card card-b">
    <div class="card-backdrop" role="img" aria-label="Blue-toned photograph of a tablet and a target graphic"></div>
    <div class="card-masthead">
      <p class="show-label">PODCAST</p>
      <p class="show-name">CHARTING HEADWAYS</p>
      <p class="show-tagline">A CEO GROWTH AND LEGACY</p>
      <div class="masthead-mark"></div>
    </div>
    <h2 class="episode-title">Technology<br>a Philanthropy<br>in Education</h2>
    <div class="guest-portrait" role="img" aria-label="Guest portrait photograph"></div>
    <p class="guest-credit">With Tomas Reller<br><span class="guest-role">CEO of Veltra</span></p>
    <div class="card-signature"><span class="signature-dot"></span><span class="signature-name">LENNART OSWALD ADVISORY</span></div>
  </article>

  <article class="episode-card card-c">
    <div class="card-backdrop" role="img" aria-label="Blue-toned photograph of a laptop keyboard"></div>
    <div class="card-masthead">
      <p class="show-label">PODCAST</p>
      <p class="show-name">CHARTING HEADWAYS</p>
      <p class="show-tagline">A CEO GROWTH AND LEGACY</p>
      <div class="masthead-mark"></div>
    </div>
    <h2 class="episode-title">Technology<br>a Philanthropy<br>in Education</h2>
    <div class="guest-portrait" role="img" aria-label="Guest portrait photograph"></div>
    <p class="guest-credit">With Tomas Reller<br><span class="guest-role">CEO of Veltra</span></p>
    <div class="card-signature"><span class="signature-dot"></span><span class="signature-name">LENNART OSWALD ADVISORY</span></div>
  </article>

  <article class="episode-card card-d">
    <div class="card-backdrop" role="img" aria-label="Blue-toned photograph of city towers at night"></div>
    <div class="card-masthead">
      <p class="show-label">PODCAST</p>
      <p class="show-name">CHARTING HEADWAYS</p>
      <p class="show-tagline">A CEO GROWTH AND LEGACY</p>
      <div class="masthead-mark"></div>
    </div>
    <h2 class="episode-title">Technology<br>a Philanthropy<br>in Education</h2>
    <div class="guest-portrait" role="img" aria-label="Guest portrait photograph"></div>
    <p class="guest-credit">With Tomas Reller<br><span class="guest-role">CEO of Veltra</span></p>
    <div class="card-signature"><span class="signature-dot"></span><span class="signature-name">LENNART OSWALD ADVISORY</span></div>
  </article>
</body>
</html>
```